Marwick Estate Services (Handyman / Home Improvement Company)

Looking for a double sided professional looking business card with Logo attached to be highlighted on one side and throwing in an image of a handyman as an option would be nice to see as well. We are a company focused on providing quality Handyman and Home improvement services in a timely manner that is done right the first time with integrity

Industry/Entity Type

Handyman / Home Improvement

Contact Information for Business Card

(LOGO, Name, Mobile and office phone numbers, email) on front side of card, (the words "The SOLUTION to all of your Handyman and Home Improvement needs" followed by "Family Owned and Operated" at the very bottom) on the back.

Colors
EB3D1F
EC4F4E
F09395
F8D3D4
FCEDEE

Requirements
Must have
• Red, Gray, Black Color scheme
Should not have
• No Yellow or Blue colors

```html
<!DOCTYPE html>
<html lang="en">
<head>
<meta charset="utf-8">
<title>Marwick Estate Services – Business Card</title>
<link href="https://fonts.googleapis.com/css2?family=Roboto:wght@400;500;700&display=swap" rel="stylesheet">
<style>
  :root {
    --bg: #d9d9db;
    --black: #0d0d0d;
    --band: #070707;
    --red: #eb3d1f;
    --red-bright: #e8322f;
    --red-deep: #a5141a;
    --white: #ffffff;
    --rule: #d8262b;
  }
  * { box-sizing: border-box; margin: 0; padding: 0; }
  html, body { width: 1200px; height: 801px; overflow: hidden; }
  body {
    background: var(--bg);
    font-family: "Roboto", Arial, sans-serif;
    display: flex;
    align-items: center;
    justify-content: center;
    gap: 40px;
  }
  .card {
    width: 540px;
    height: 310px;
    border-radius: 22px;
    position: relative;
    overflow: hidden;
  }

  /* Front */
  .card-front {
    background: var(--black);
    color: var(--white);
    display: flex;
  }
  .front-brand {
    width: 270px;
    display: flex;
    align-items: center;
    justify-content: center;
    gap: 12px;
    padding-left: 24px;
  }
  .brand-dot {
    width: 22px; height: 22px;
    border-radius: 50%;
    background: var(--red);
    flex: none;
  }
  .brand-name {
    font-weight: 700;
    font-size: 22px;
    line-height: 1.15;
    text-transform: uppercase;
    color: var(--white);
  }
  .front-contact {
    flex: 1;
    padding: 50px 30px 0 6px;
  }
  .person-name { font-size: 28px; font-weight: 500; }
  .person-role {
    font-size: 12px; color: var(--red); text-transform: uppercase;
    letter-spacing: .3px; margin-top: 2px;
  }
  .rule { height: 1px; background: var(--rule); margin: 12px 0; }
  .contact-list { list-style: none; font-size: 13px; }
  .contact-list li { display: flex; align-items: center; gap: 9px; margin: 6px 0; }
  .contact-list svg { width: 14px; height: 14px; flex: none; }
  .address { font-size: 13px; line-height: 1.4; }

  /* Back */
  .card-back {
    background: linear-gradient(160deg, var(--red-bright) 20%, var(--red-deep) 95%);
  }
  .back-brand {
    position: absolute; left: 0; right: 0; top: 0; height: 210px;
    display: flex; align-items: center; justify-content: center; gap: 14px;
  }
  .back-brand .brand-name { color: var(--black); font-size: 30px; }
  .back-brand .brand-dot { background: var(--black); width: 28px; height: 28px; }
  .tagline-band {
    position: absolute; left: 0; right: 0; bottom: 0; height: 100px;
    background: var(--band);
    color: var(--white);
    display: flex; flex-direction: column; align-items: center; justify-content: center;
    text-transform: uppercase; letter-spacing: 1.4px; font-weight: 500;
    text-align: center;
  }
  .tagline-main { font-size: 12.5px; }
  .tagline-sub { font-size: 12.5px; margin-top: 6px; }
</style>
</head>
<body>
  <section class="card card-front">
    <div class="front-brand">
      <span class="brand-dot"></span>
      <span class="brand-name">Marwick Estate<br>Services</span>
    </div>
    <div class="front-contact">
      <h1 class="person-name">Daniel Marwick</h1>
      <p class="person-role">Your Designation</p>
      <div class="rule"></div>
      <ul class="contact-list">
        <li>
          <svg viewBox="0 0 24 24"><path fill="#eb3d1f" d="M6.6 10.8a15 15 0 0 0 6.6 6.6l2.2-2.2a1 1 0 0 1 1-.25 11.4 11.4 0 0 0 3.6.57 1 1 0 0 1 1 1V20a1 1 0 0 1-1 1A17 17 0 0 1 3 4a1 1 0 0 1 1-1h3.5a1 1 0 0 1 1 1c0 1.25.2 2.45.57 3.57a1 1 0 0 1-.25 1z"/></svg>
          555-204-7781 (Mobile)
        </li>
        <li>
          <svg viewBox="0 0 24 24"><rect x="3" y="8" width="18" height="12" rx="2" fill="#eb3d1f"/><rect x="6" y="3" width="12" height="6" rx="1" fill="#eb3d1f"/></svg>
          555-204-7782 (Office)
        </li>
        <li>
          <svg viewBox="0 0 24 24"><circle cx="12" cy="12" r="9" fill="none" stroke="#eb3d1f" stroke-width="2.4"/><circle cx="12" cy="12" r="3.5" fill="none" stroke="#eb3d1f" stroke-width="2.4"/></svg>
          info@marwickestate.com
        </li>
      </ul>
      <div class="rule"></div>
      <p class="address">48 Alder Lane, Brookfield,<br>CT 06804, USA</p>
    </div>
  </section>

  <section class="card card-back">
    <div class="back-brand">
      <span class="brand-dot"></span>
      <span class="brand-name">Marwick Estate<br>Services</span>
    </div>
    <div class="tagline-band">
      <p class="tagline-main">Your solution to all of your handyman and home improvement needs</p>
      <p class="tagline-sub">Family owned and operated</p>
    </div>
  </section>
</body>
</html>
```